Website Redesign for an Appointment Setting and Lead Generation Company.

I need to redesign an existing website. The website that we are looking to be redesigned is www.trellisvane.example. TrellisVane is a B2B appointment setting organization. The idea is to present a modern look website for professional services company. The idea is to engage the user, look at various services and generate more inbound leads for the website

Target Market(s)

US, APAC, Europe, UK. Focused on B2B companies more than $100 Mn

Industry/Entity Type

Professional Service

Number of Pages Required

5+ page

Font styles to use
Other font styles liked:
• Roboto

Requirements
Must have
• Home Page - Banner Image, Section for Client testimonials
Industry Page - To show industry capabilities
Services Page - To show service capabilities
Blogs Page - to show blogs
Offerings Page - Offerings Page
Nice to have
• I would like to have a elegant design with small animation. Preferably use colors from the logo attached. Use infographics where possible

```html
<!DOCTYPE html>
<html lang="en">
<head>
<meta charset="utf-8">
<title>TrellisVane — B2B Appointment Setting &amp; Lead Generation</title>
<link rel="stylesheet" href="https://fonts.googleapis.com/css2?family=Montserrat:ital,wght@0,400;0,500;0,600;0,700;1,400&display=swap">
<style>
:root{
  --red:#d7363b;
  --red-dark:#b32a2f;
  --ink:#222;
  --text:#444;
  --muted:#888;
  --soft:#f0f0f0;
  --field:#fbe8e8;
  --footer:#262626;
  --line:#ddd;
}
*{box-sizing:border-box;margin:0;padding:0}
html,body{width:1200px;height:3742px;overflow:hidden;background:#fff}
body{font-family:"Montserrat",sans-serif;color:var(--text)}
.page{position:relative;width:1200px;height:3742px;overflow:hidden}
.abs{position:absolute}
.center{text-align:center}

/* top bar */
.topbar{top:0;left:0;width:1200px;height:29px;background:var(--red);color:#fff;font-size:8px}
.topbar .item{position:absolute;top:9px;display:flex;align-items:center;gap:6px}
.topbar .search{position:absolute;left:757px;top:7px;width:187px;height:15px;background:#fff;border-radius:8px;color:#999;font-size:7px;padding:3px 10px}
.topbar .search svg{position:absolute;right:10px;top:3px}
.topbar .social{position:absolute;top:6px;width:22px;height:16px;background:#fff;border-radius:5px}

/* header */
.header{top:29px;left:0;width:1200px;height:68px;background:#fff}
.brand{position:absolute;display:flex;align-items:center;gap:8px;font-weight:700;color:var(--red)}
.brand .mark{width:18px;height:18px;background:var(--red)}
.header .brand{left:150px;top:20px;font-size:24px}
.nav{position:absolute;top:27px;font-size:11px;color:#333}
.nav.active{color:var(--red)}
.btn{position:absolute;display:flex;align-items:center;justify-content:center;background:var(--red);color:#fff;border-radius:20px;font-weight:600}
.header .btn{left:944px;top:22px;width:105px;height:23px;font-size:11px}

/* hero */
.hero{top:97px;left:0;width:1200px;height:281px;background:linear-gradient(100deg,#1f1f1f 0%,#2b2b2b 35%,#6a5a52 65%,#8c7b72 100%)}
.hero h1{position:absolute;left:150px;top:55px;color:#fff;font-size:24px;font-weight:700;line-height:28px;letter-spacing:.3px}
.hero p{position:absolute;left:150px;top:122px;width:520px;color:#eee;font-size:11px;line-height:17px}
.hero .btn{left:150px;top:193px;width:150px;height:26px;font-size:11px}

/* section titles */
.title{position:absolute;left:0;width:1200px;display:flex;justify-content:center;align-items:center;gap:18px;font-size:22px;font-weight:600;color:var(--ink)}
.title span.r{color:var(--red)}
.title::before,.title::after{content:"";width:75px;height:1px;background:var(--red)}

.about{top:378px;left:0;width:1200px;height:436px}
.about .lead{position:absolute;left:250px;top:56px;width:700px;font-size:11px;line-height:17px;text-align:center;color:#444}
.subhead{position:absolute;left:0;width:1200px;text-align:center;font-size:13px;font-weight:600;color:var(--ink)}
.cap{position:absolute;top:199px;width:210px;text-align:center}
.cap .ring{position:relative;width:208px;height:126px;margin:0 auto}
.cap .ring svg{position:absolute;left:0;top:0}
.cap .pct{position:absolute;left:0;width:208px;top:34px;font-size:21px;font-weight:600;color:var(--red)}
.cap .lbl{position:absolute;left:40px;width:128px;top:62px;font-size:7px;font-weight:600;line-height:10px;color:#333}
.cap h4{margin-top:12px;font-size:11px;font-weight:600;color:#222}
.cap p{margin-top:4px;font-size:9px;line-height:11px;color:#999}

/* services */
.services{top:814px;left:0;width:1200px;height:489px;background:var(--soft)}
.stat{position:absolute;width:262px;height:160px}
.stat svg{position:absolute;left:0;top:0}
.stat .num{position:absolute;left:0;width:262px;top:44px;text-align:center;color:#fff;font-size:26px;font-weight:600}
.stat .bar{position:absolute;left:121px;top:84px;width:20px;height:1px;background:#f3a6a8}
.stat .lbl{position:absolute;left:0;width:262px;top:92px;text-align:center;color:#fff;font-size:11px;font-weight:600;line-height:14px}

/* blog */
.blog{top:1303px;left:0;width:1200px;height:477px}
.post{position:absolute;top:82px;width:284px;height:290px;border:1px solid #ddd;border-radius:22px;overflow:hidden;background:#fff;box-shadow:0 2px 6px rgba(0,0,0,.08);text-align:center}
.post .img{height:126px}
.post h3{margin-top:8px;font-size:11.5px;font-weight:500;color:var(--red)}
.post .meta{margin-top:3px;font-size:6.5px;color:#777}
.post .meta b{color:var(--red);font-weight:400}
.post p{margin:8px 18px 0;font-size:9.3px;line-height:12.2px;color:#444}
.post .more{margin-top:5px;font-size:9.5px;color:var(--red);letter-spacing:.4px}
.post .date{position:absolute;left:0;bottom:8px;width:284px;border-top:1px solid #e3e3e3;padding-top:6px;font-size:6px;color:#888;margin:0}
.blog .btn{left:525px;top:401px;width:149px;height:28px;font-size:11.5px}

/* offers */
.offers{top:1780px;left:0;width:1200px;height:450px;background:var(--soft)}
.offers .lead{position:absolute;left:218px;top:72px;width:764px;text-align:center;font-size:11px;line-height:17px;color:#444}
.offers .lead b{color:var(--red);font-weight:600}
.offer{position:absolute;top:237px;width:270px;height:167px;background:#fff;border-radius:20px;box-shadow:0 4px 10px rgba(0,0,0,.12);text-align:center}
.offer h4{margin-top:26px;font-size:11px;font-weight:500;color:#333;letter-spacing:.3px}
.offer p{margin:14px 26px 0;font-size:6.5px;line-height:10px;color:#999}
.offer .lm{display:inline-block;margin-top:8px;width:84px;height:15px;line-height:13px;border:1px solid var(--red);border-radius:10px;font-size:5.5px;color:var(--red)}
.offer .lm.on{background:var(--red);color:#fff}

/* testimonials */
.testi{top:2230px;left:0;width:1200px;height:334px}
.testi .sub{position:absolute;left:0;width:1200px;top:84px;text-align:center;font-size:15px;color:#444;letter-spacing:.5px}
.quote{position:absolute;left:161px;top:119px;width:878px;height:169px;border:1px solid #ddd;border-radius:22px;background:#fff}
.quote .q{position:absolute;left:130px;top:24px;width:618px;text-align:center;font-size:13.5px;font-style:italic;line-height:20px;color:#999;letter-spacing:.4px}
.quote .qm{position:absolute;font-size:26px;font-weight:700;color:var(--red);line-height:1}
.quote .avatar{position:absolute;left:352px;top:82px;width:90px;height:58px;border-radius:50%;background:linear-gradient(160deg,#e4e4e4,#9a9a9a)}
.quote .who{position:absolute;left:458px;top:97px;font-size:10.5px;color:#333}
.quote .who span{display:block;margin-top:4px;font-size:8.5px;color:#999}
.arrow{position:absolute;top:73px;width:38px;height:22px;border-radius:50%}

/* newsletter */
.news{top:2564px;left:0;width:1200px;height:116px;background:linear-gradient(180deg,#e03a3f,#d1343a)}
.news h3{position:absolute;left:202px;top:43px;color:#fff;font-size:16px;font-weight:700;letter-spacing:.3px}
.news p{position:absolute;left:202px;top:64px;color:#fde;font-size:8px}
.news .input{position:absolute;left:559px;top:47px;width:308px;height:25px;background:#fff;border-radius:13px 0 0 13px;font-size:8px;color:#bbb;padding:8px 18px}
.news .go{position:absolute;left:867px;top:47px;width:130px;height:25px;background:#1c1c1c;border-radius:0 13px 13px 0;color:#fff;font-size:9.5px;font-weight:600;display:flex;align-items:center;justify-content:center}

/* contact */
.contact{top:2680px;left:0;width:1200px;height:564px}
.contact .sub{position:absolute;left:0;width:1200px;top:78px;text-align:center;font-size:15px;color:#444;letter-spacing:1px}
.field{position:absolute;background:var(--field);border-radius:18px;font-size:12px;color:#aaa;padding:10px 21px;letter-spacing:.8px}
.field i{font-style:normal;color:var(--red)}
.consent{position:absolute;left:203px;top:358px;font-size:11.5px;font-weight:500;color:#333;display:flex;align-items:center;gap:14px;letter-spacing:.5px}
.consent .box{width:12px;height:11px;background:var(--red);border-radius:2px;display:flex;align-items:center;justify-content:center}
.contact .small{position:absolute;left:203px;width:794px;font-size:12px;line-height:15px;color:#444;letter-spacing:.8px}
.contact .small b{color:var(--red)}
.contact .btn{left:525px;top:493px;width:149px;height:26px;font-size:12px}

/* map */
.map{top:3244px;left:0;width:1200px;height:257px;background:linear-gradient(135deg,#dcdcdc,#c8c8c8 50%,#e2e2e2)}
.info{position:absolute;left:150px;top:22px;width:351px;height:216px;background:#fff;border-radius:40px}
.info .row{position:absolute;left:62px;display:flex;gap:18px;align-items:flex-start;font-size:8px;color:#333}
.info .row div{line-height:10px}
.info .row small{display:block;color:#555;font-size:7.5px}
.info .row .ic{width:20px;display:flex;justify-content:center}
.info .sep{position:absolute;left:40px;width:275px;height:1px;background:#eee}
.pinlabel{position:absolute;left:702px;top:100px;display:flex;align-items:center;gap:10px;color:var(--red);font-size:16px;font-weight:700;letter-spacing:1.5px}

/* footer */
.footer{top:3501px;left:0;width:1200px;height:241px;background:var(--footer);color:#ddd}
.footer .brand{left:150px;top:34px;font-size:22px}
.footer .about{position:absolute;left:150px;top:84px;width:280px;font-size:7.5px;line-height:13px;color:#ddd;height:auto}
.footer .soc{position:absolute;top:149px;width:20px;height:14px;border-radius:5px}
.fcol{position:absolute;top:54px}
.fcol h5{font-size:14px;font-weight:500;color:#fff;letter-spacing:1px;margin-bottom:8px}
.fcol li{list-style:none;font-size:7px;line-height:14px;color:#ddd}
.fcol li::before{content:"› ";}
.fcol li.on{color:var(--red)}
.footer .rule{position:absolute;left:150px;top:207px;width:900px;height:1px;background:#555}
.footer .copy{position:absolute;left:0;width:1200px;top:222px;text-align:center;font-size:7px;color:#ccc}
</style>
</head>
<body>
<div class="page">

  <!-- top bar -->
  <div class="abs topbar">
    <div class="item" style="left:150px">
      <svg width="10" height="7" viewBox="0 0 10 7"><rect width="10" height="7" rx="1" fill="#fff"/></svg>
      info@trellisvane.example</div>
    <div class="item" style="left:300px">
      <svg width="9" height="9" viewBox="0 0 24 24"><path fill="#fff" d="M6.6 10.8a15 15 0 0 0 6.6 6.6l2.2-2.2c.3-.3.7-.4 1-.2 1.1.4 2.3.6 3.6.6.6 0 1 .4 1 1V20c0 .6-.4 1-1 1A17 17 0 0 1 3 4c0-.6.4-1 1-1h3.5c.6 0 1 .4 1 1 0 1.3.2 2.5.6 3.6.1.3 0 .7-.2 1z"/></svg>
      +1 555-010-4821</div>
    <div class="item" style="left:408px">
      <svg width="9" height="9" viewBox="0 0 10 10"><circle cx="5" cy="5" r="4.5" fill="#fff"/><path d="M5 2.5V5l1.8 1" stroke="#d7363b" fill="none"/></svg>
      Mon - Fri: 9:00 am - 6:00 pm</div>
    <div class="search">Search Something
      <svg width="9" height="9" viewBox="0 0 10 10"><circle cx="4" cy="4" r="3" stroke="#555" fill="none"/><path d="M6.3 6.3 9 9" stroke="#555"/></svg></div>
    <div class="social" style="left:967px"></div>
    <div class="social" style="left:996px"></div>
    <div class="social" style="left:1027px"></div>
  </div>

  <!-- header -->
  <header class="abs header">
    <div class="brand"><span class="mark"></span>TrellisVane</div>
    <span class="nav" style="left:487px">Home</span>
    <span class="nav" style="left:539px">About ▾</span>
    <span class="nav active" style="left:600px">Services ▾</span>
    <span class="nav" style="left:677px">Our Expertise ▾</span>
    <span class="nav" style="left:782px">Library ▾</span>
    <span class="nav" style="left:848px">Contact Us ▾</span>
    <span class="btn">Contact Us</span>
  </header>

  <!-- hero -->
  <section class="abs hero" role="img" aria-label="Team stacking hands together in the center, dark toned photo">
    <h1>Build your Sales Pipeline<br>in the New Normal!</h1>
    <p>Providing end-to-end webinar management services - including platform support, audience acquisition, providing subject matter expert speakers, webinar moderation, reporting, and lead nurturing on the webinar attendees.</p>
    <span class="btn">Read More</span>
  </section>

  <!-- industry -->
  <section class="abs about">
    <h2 class="title" style="top:12px">About Our <span class="r">Industry</span></h2>
    <p class="lead">As the needs of your clients evolve, so should your service offerings. Our capabilities boost your sales pipeline for global outreach and give you an edge over your competitors. To understand your prospects' needs and your service offerings, TrellisVane' executives are regularly trained on domains and next-generation service offerings. Our capabilities include delivering campaigns in local languages across continents &amp; expertise in next-gen offerings like ML/AI/RPA. This is a testament based on the campaigns we delivered in the last one year.</p>
    <div class="subhead" style="top:163px">Our Industry Capabilities</div>

    <div class="cap" style="left:149px">
      <div class="ring">
        <svg width="208" height="126" viewBox="0 0 208 126"><ellipse cx="104" cy="63" rx="101" ry="60" fill="none" stroke="#e2e2e2" stroke-width="3"/><path d="M104 3A101 60 0 1 1 104 123A101 60 0 1 1 104 3" pathLength="100" fill="none" stroke="#d7363b" stroke-width="3" stroke-dasharray="22 100"/></svg>
        <div class="pct">22%</div><div class="lbl">Multilingual Campaigns Executed by Onsite Resources</div>
      </div>
      <h4>Lorem ipsum dolor sit amet</h4><p>Lorem ipsum dolor sit amet,<br>consectetur adipiscing elit,<br>sed do eiusmod</p>
    </div>
    <div class="cap" style="left:379px">
      <div class="ring">
        <svg width="208" height="126" viewBox="0 0 208 126"><ellipse cx="104" cy="63" rx="101" ry="60" fill="none" stroke="#e2e2e2" stroke-width="3"/><path d="M104 3A101 60 0 1 1 104 123A101 60 0 1 1 104 3" pathLength="100" fill="none" stroke="#d7363b" stroke-width="3" stroke-dasharray="35 100"/></svg>
        <div class="pct">35%</div><div class="lbl">Campaigns on Traditional IT &amp; Infrastructure Management Services</div>
      </div>
      <h4>Lorem ipsum dolor sit amet</h4><p>Lorem ipsum dolor sit amet,<br>consectetur adipiscing elit,<br>sed do eiusmod</p>
    </div>
    <div class="cap" style="left:608px">
      <div class="ring">
        <svg width="208" height="126" viewBox="0 0 208 126"><ellipse cx="104" cy="63" rx="101" ry="60" fill="none" stroke="#e2e2e2" stroke-width="3"/><path d="M104 3A101 60 0 1 1 104 123A101 60 0 1 1 104 3" pathLength="100" fill="none" stroke="#d7363b" stroke-width="3" stroke-dasharray="65 100"/></svg>
        <div class="pct">65%</div><div class="lbl">Campaigns on AI/ML/RPA, Product Engineering &amp; Digital Transformation</div>
      </div>
      <h4>Lorem ipsum dolor sit amet</h4><p>Lorem ipsum dolor sit amet,<br>consectetur adipiscing elit,<br>sed do eiusmod</p>
    </div>
    <div class="cap" style="left:841px">
      <div class="ring">
        <svg width="208" height="126" viewBox="0 0 208 126"><ellipse cx="104" cy="63" rx="101" ry="60" fill="none" stroke="#e2e2e2" stroke-width="3"/><path d="M104 3A101 60 0 1 1 104 123A101 60 0 1 1 104 3" pathLength="100" fill="none" stroke="#d7363b" stroke-width="3" stroke-dasharray="25 100"/></svg>
        <div class="pct">25%</div><div class="lbl">Campaigns on Events Audience Acquisition</div>
      </div>
      <h4>Lorem ipsum dolor sit amet</h4><p>Lorem ipsum dolor sit amet,<br>consectetur adipiscing elit,<br>sed do eiusmod</p>
    </div>
  </section>

  <!-- services -->
  <section class="abs services">
    <h2 class="title" style="top:40px">Our <span class="r">Services</span></h2>
    <svg width="0" height="0" style="position:absolute"><defs>
      <symbol id="disc" viewBox="0 0 262 160"><ellipse cx="131" cy="80" rx="129" ry="78" fill="#b8262c"/><ellipse cx="131" cy="80" rx="124" ry="74" fill="#cf343a"/><ellipse cx="131" cy="80" rx="116" ry="68" fill="#cf343a" stroke="#f2b2b4" stroke-width="1"/></symbol>
    </defs></svg>
    <div class="stat" style="left:149px;top:82px"><svg width="262" height="160"><use href="#disc"/></svg><div class="num">3800</div><div class="bar"></div><div class="lbl">Research Reports<br>Generated</div></div>
    <div class="stat" style="left:469px;top:82px"><svg width="262" height="160"><use href="#disc"/></svg><div class="num">80%</div><div class="bar"></div><div class="lbl">Client Retention<br>Rate</div></div>
    <div class="stat" style="left:787px;top:82px"><svg width="262" height="160"><use href="#disc"/></svg><div class="num">500+</div><div class="bar"></div><div class="lbl">Surveys and Interviews<br>conducted per month</div></div>
    <div class="stat" style="left:149px;top:280px"><svg width="262" height="160"><use href="#disc"/></svg><div class="num">50%</div><div class="bar"></div><div class="lbl">Leads Generated<br>with CXOs &amp; VPs</div></div>
    <div class="stat" style="left:469px;top:280px"><svg width="262" height="160"><use href="#disc"/></svg><div class="num">33</div><div class="bar"></div><div class="lbl">Events<br>Managed</div></div>
    <div class="stat" style="left:787px;top:280px"><svg width="262" height="160"><use href="#disc"/></svg><div class="num">20</div><div class="bar"></div><div class="lbl">Databases<br>Subscribed</div></div>
  </section>

  <!-- blog -->
  <section class="abs blog">
    <h2 class="title" style="top:40px">Latest Blog <span class="r">Posts</span></h2>
    <article class="post" style="left:150px">
      <div class="img" role="img" aria-label="Business team meeting around an office table" style="background:linear-gradient(180deg,#e9ecef,#b9bec4 60%,#7d838a)"></div>
      <h3>Sed ut perspiciatis unde omnis</h3>
      <div class="meta">Posted by <b>TrellisVane</b> &nbsp;|&nbsp; <b>9 Comments</b></div>
      <p>Lorem ipsum dolor sit amet, consectetur adipiscing elit, sed do eiusmod tempor incididunt ut labore et dolore magna aliqua. Ut enim ad minim veniam, quis nostrud exercitation ullamco laboris nisi ut aliquip ex commodo consequat. Duis aute irure dolor in reprehenderit velit esse cillum dolore eu fugiat nulla pariatur.</p>
      <div class="more">Read More...</div>
      <div class="date">November 20, 2020</div>
    </article>
    <article class="post" style="left:458px">
      <div class="img" role="img" aria-label="Glass skyscrapers seen from below against a blue sky" style="background:linear-gradient(180deg,#8fb2cf,#3f5f7c 55%,#1f2f3e)"></div>
      <h3>Sed ut perspiciatis unde omnis</h3>
      <div class="meta">Posted by <b>TrellisVane</b> &nbsp;|&nbsp; <b>9 Comments</b></div>
      <p>Lorem ipsum dolor sit amet, consectetur adipiscing elit, sed do eiusmod tempor incididunt ut labore et dolore magna aliqua. Ut enim ad minim veniam, quis nostrud exercitation ullamco laboris nisi ut aliquip ex commodo consequat. Duis aute irure dolor in reprehenderit velit esse cillum dolore eu fugiat nulla pariatur.</p>
      <div class="more">Read More...</div>
      <div class="date">November 20, 2020</div>
    </article>
    <article class="post" style="left:765px">
      <div class="img" role="img" aria-label="Hands reviewing printed charts on a desk" style="background:linear-gradient(180deg,#dfe6ef,#b3c2d6 60%,#d9c7b6)"></div>
      <h3>Sed ut perspiciatis unde omnis</h3>
      <div class="meta">Posted by <b>TrellisVane</b> &nbsp;|&nbsp; <b>9 Comments</b></div>
      <p>Lorem ipsum dolor sit amet, consectetur adipiscing elit, sed do eiusmod tempor incididunt ut labore et dolore magna aliqua. Ut enim ad minim veniam, quis nostrud exercitation ullamco laboris nisi ut aliquip ex commodo consequat. Duis aute irure dolor in reprehenderit velit esse cillum dolore eu fugiat nulla pariatur.</p>
      <div class="more">Read More...</div>
      <div class="date">November 20, 2020</div>
    </article>
    <span class="btn">See More</span>
  </section>

  <!-- offers -->
  <section class="abs offers">
    <h2 class="title" style="top:40px">Our <span class="r">Offers</span></h2>
    <p class="lead">We are a leading B2B lead generation company with presence across North America, Europe, APAC and India. Our experienced and trained lead generation executives understand your unique service offerings and work along your campaign journey to achieve the desired goals. Leveraging our extensive proprietary database, we target key decision-makers &amp; influencers across industries. Our sales lead generation services are custom-made for your service offerings, be it next-generation technologies like machine learning, digital transformation, analytics, and artificial intelligence. We work as an extension of your team and deliver results that matter to your business.<br><b>Improve Sales Pipeline and Acquire New Customers.</b></p>
    <div class="offer" style="left:150px"><h4>GLOBAL PARTNER</h4><p>Lorem ipsum dolor sit amet, consectetur adipiscing elit, sed do eiusmod tempor incididunt ut labore et dolore magna aliqua. Ut enim ad minim veniam, quis nostrud exercitation ullamco laboris nisi ut aliquip ex ea commodo consequat.</p><span class="lm">Learn More</span></div>
    <div class="offer" style="left:465px"><h4>DOMAIN EXPERTISE</h4><p>Lorem ipsum dolor sit amet, consectetur adipiscing elit, sed do eiusmod tempor incididunt ut labore et dolore magna aliqua. Ut enim ad minim veniam, quis nostrud exercitation ullamco laboris nisi ut aliquip ex ea commodo consequat.</p><span class="lm on">Learn More</span></div>
    <div class="offer" style="left:780px"><h4>PROPRIETARY SYSTEMS</h4><p>Lorem ipsum dolor sit amet, consectetur adipiscing elit, sed do eiusmod tempor incididunt ut labore et dolore magna aliqua. Ut enim ad minim veniam, quis nostrud exercitation ullamco laboris nisi ut aliquip ex ea commodo consequat.</p><span class="lm">Learn More</span></div>
  </section>

  <!-- testimonials -->
  <section class="abs testi">
    <h2 class="title" style="top:40px">Our <span class="r">Testimonials</span></h2>
    <div class="sub">What our customer saying?</div>
    <div class="quote">
      <span class="qm" style="left:102px;top:20px">“</span>
      <span class="qm" style="left:757px;top:20px">”</span>
      <p class="q">Lorem ipsum dolor sit amet, consectetur adipiscing elit, sed do eiusmod tempor incididunt utlabore et dolore magna aliqua.</p>
      <svg class="arrow" style="left:30px" width="38" height="22" viewBox="0 0 38 22"><ellipse cx="19" cy="11" rx="18" ry="10" fill="#fff" stroke="#d7363b"/><path d="M25 11H13M17 7l-4 4 4 4" stroke="#d7363b" fill="none"/></svg>
      <svg class="arrow" style="left:810px" width="38" height="22" viewBox="0 0 38 22"><ellipse cx="19" cy="11" rx="18.5" ry="10.5" fill="#d7363b"/><path d="M13 11h12M21 7l4 4-4 4" stroke="#fff" fill="none"/></svg>
      <div class="avatar" role="img" aria-label="Client portrait"></div>
      <div class="who">Marcus Hale<span>CEO of Northwind Motors</span></div>
    </div>
  </section>

  <!-- newsletter -->
  <section class="abs news">
    <h3>Subscribe to our newsletter</h3>
    <p>Subcribe to our newsletter to get the lastest scoop right to your inbox</p>
    <div class="input">Your Email Address</div>
    <div class="go">Subscribe</div>
  </section>

  <!-- contact -->
  <section class="abs contact">
    <h2 class="title" style="top:40px">Contact <span class="r">Us</span></h2>
    <div class="sub">Fill in The Form Below</div>
    <div class="field" style="left:203px;top:120px;width:384px;height:33px">First Name<i>*</i></div>
    <div class="field" style="left:612px;top:120px;width:385px;height:33px">Last Name<i>*</i></div>
    <div class="field" style="left:203px;top:170px;width:384px;height:34px">Email Address<i>*</i></div>
    <div class="field" style="left:612px;top:170px;width:385px;height:34px">Phone Number<i>*</i></div>
    <div class="field" style="left:203px;top:221px;width:794px;height:34px">Company Name<i>*</i></div>
    <div class="field" style="left:203px;top:272px;width:794px;height:73px">Message<i>*</i></div>
    <div class="consent"><span class="box"><svg width="8" height="6" viewBox="0 0 8 6"><path d="M1 3l2 2 4-4" stroke="#fff" fill="none" stroke-width="1.3"/></svg></span>I agree to receive other communications from TrellisVane.</div>
    <p class="small" style="top:389px">You can unsubscribe from these communications at any time. For more information on how to unsubscribe, our privacy practices, and how we are committed to protecting and respecting your privacy, please review our <b>Privacy Policy</b>.</p>
    <p class="small" style="top:441px">By clicking submit below, you consent to allow TrellisVane to store and process the personal information submitted above to provide you the content requested.</p>
    <span class="btn">Submit</span>
  </section>

  <!-- map -->
  <section class="abs map" role="img" aria-label="Grey street map of the office area">
    <div class="info">
      <div class="row" style="top:20px"><span class="ic"><svg width="20" height="14" viewBox="0 0 20 14"><ellipse cx="10" cy="7" rx="9" ry="6" fill="none" stroke="#d7363b" stroke-width="1.3"/><path d="M7 10l2-5 4-1-2 5z" fill="none" stroke="#d7363b"/></svg></span><div>Visit our location<small>Your Address, City State Zip Code</small></div></div>
      <div class="sep" style="top:52px"></div>
      <div class="row" style="top:62px"><span class="ic"><svg width="12" height="18" viewBox="0 0 12 18"><rect x="1" y="1" width="10" height="16" rx="2" fill="none" stroke="#d7363b" stroke-width="1.3"/><path d="M5 14h2" stroke="#d7363b"/></svg></span><div>Give us a Call<small>+1 555-010-4821</small></div></div>
      <div class="sep" style="top:94px"></div>
      <div class="row" style="top:104px"><span class="ic"><svg width="18" height="18" viewBox="0 0 18 18"><path d="M4 13V8a5 5 0 0 1 10 0v5l2 2H2z" fill="none" stroke="#d7363b" stroke-width="1.3"/><path d="M7 16h4" stroke="#d7363b"/></svg></span><div>Opening Hours<small>Mon - Fri: 9:00 - 19:00<br>Closed on Weekends</small></div></div>
      <div class="sep" style="top:146px"></div>
      <div class="row" style="top:160px"><span class="ic"><svg width="20" height="16" viewBox="0 0 20 16"><path d="M1 7L19 1l-6 14-3-6z M10 9l9-8" fill="none" stroke="#d7363b" stroke-width="1.3"/></svg></span><div>Email<small>info@trellisvane.example</small></div></div>
    </div>
    <div class="pinlabel"><svg width="32" height="36" viewBox="0 0 32 36"><ellipse cx="16" cy="31" rx="12" ry="4" fill="#999"/><path d="M16 32C8 22 5 17 5 12a11 11 0 0 1 22 0c0 5-3 10-11 20z" fill="#2a2a2a"/><circle cx="16" cy="12" r="4" fill="#fff"/></svg>TrellisVane</div>
  </section>

  <!-- footer -->
  <footer class="abs footer">
    <div class="brand"><span class="mark"></span>TrellisVane</div>
    <p class="about">WE ARE A LEADING B2B LEAD GENERATION COMPANY WITH PRESENCE ACROSS NORTH AMERICA, EUROPE, APAC AND INDIA. OUR EXPERIENCED AND TRAINED LEAD GENERATION EXECUTIVES UNDERSTAND YOUR UNIQUE SERVICE OFFERINGS AND WORK ALONG YOUR CAMPAIGN JOURNEY TO ACHIEVE THE DESIRED GOALS.</p>
    <span class="soc" style="left:152px;background:var(--red)"></span>
    <span class="soc" style="left:180px;background:#fff"></span>
    <span class="soc" style="left:211px;background:#fff"></span>
    <div class="fcol" style="left:472px"><h5>ABOUT US</h5><ul><li class="on">HOME</li><li>ABOUT</li><li>OUR TEAM</li><li>AWARDS</li><li>OUR PARTNERSHIPS</li><li>OUR DIFFERENTIATORS</li><li>LOCATIONS</li></ul></div>
    <div class="fcol" style="left:675px"><h5>SERVICES</h5><ul><li>B2B APPOINTMENT SETTING</li><li>ACCOUNT BASED MARKETING</li><li>RESEARCH AS A SERVICE</li><li>EVENT AUDIENCE ACQUISITION</li><li>STAFFING &amp; TALENT ACQUISITION</li><li>DIGITAL MARKETING</li><li>SOCIAL MEDIA RESEARCH</li><li>LEAD NURTURING</li></ul></div>
    <div class="fcol" style="left:921px"><h5>LIBRARY</h5><ul><li>VIDEOS</li><li>INFOGRAPHICS</li><li>BLOG</li><li>CASE STUDIES</li></ul></div>
    <div class="rule"></div>
    <div class="copy">Copyright © 2020 TrellisVane. All Right Reserved</div>
  </footer>

</div>
</body>
</html>
```